Flyer Design Project

I am starting a new Cake Business called "SWEET TIN JOY" and want flyers. The main product are Cupcakes and will be marketed for parties/events/celebrations to order. Other cakes can be made to order (Christmas/Birthday etc)

Industry/Entity Type

Business

Requirements
Must have
• Contact Telephone Number

```html
<!DOCTYPE html>
<html lang="en">
<head>
<meta charset="utf-8">
<title>Sweet Tin Joy – Flyers</title>
<link rel="stylesheet" href="https://fonts.googleapis.com/css2?family=Grand+Hotel&family=Quicksand:wght@500;600&display=swap">
<style>
  :root {
    --page: #eee8e3;
    --pink-deep: #f19ea4;
    --pink-mid: #f8c3c4;
    --pink-light: #fde6e3;
    --cream: #fff8f5;
    --teal: #2c8994;
    --teal-dark: #237680;
    --teal-light: #6ab8c4;
    --mint: #62c4a2;
    --white: #ffffff;
    --photo-top: #f4b3c8;
    --photo-bottom: #f8d2dc;
  }
  * { box-sizing: border-box; margin: 0; padding: 0; }
  html, body { width: 1200px; height: 900px; overflow: hidden; }
  body {
    background: var(--page);
    position: relative;
    font-family: "Quicksand", sans-serif;
  }
  .flyer {
    position: absolute;
    overflow: hidden;
    background: radial-gradient(circle at 40% 30%, var(--cream) 0%, var(--pink-light) 35%, var(--pink-mid) 70%, var(--pink-deep) 100%);
    box-shadow: 0 6px 18px rgba(80, 50, 40, 0.18);
  }
  .flyer--portrait { left: 50px; top: 140px; width: 440px; height: 620px; }
  .flyer--landscape { left: 525px; top: 225px; width: 625px; height: 440px; }

  .brand {
    position: absolute;
    font-family: "Grand Hotel", cursive;
    color: var(--teal);
    line-height: 0.9;
    text-align: center;
    display: flex;
    flex-direction: column;
    align-items: center;
  }
  .brand__dot {
    width: 22px; height: 22px; border-radius: 50%;
    background: var(--teal);
    margin-bottom: 6px;
  }
  .flyer--portrait .brand { left: 50px; top: 30px; width: 300px; font-size: 76px; }
  .flyer--landscape .brand { left: 70px; top: 24px; width: 290px; font-size: 78px; }

  .cupcake-photo {
    position: absolute;
    border-radius: 6px;
    background: linear-gradient(180deg, var(--photo-top) 0%, var(--photo-bottom) 100%);
  }
  .flyer--portrait .cupcake-photo { left: 262px; top: 245px; width: 150px; height: 200px; }
  .flyer--landscape .cupcake-photo { left: 375px; top: 44px; width: 225px; height: 232px; }

  .tagline {
    position: absolute;
    text-align: center;
    font-family: "Grand Hotel", cursive;
    line-height: 1;
  }
  .tagline__lead, .tagline__end { color: var(--mint); }
  .tagline__main { color: var(--teal); display: block; }
  .tagline__amp { color: var(--mint); }
  .tagline__end .tagline__plain { color: var(--teal); }
  .flyer--portrait .tagline { left: 20px; top: 350px; width: 240px; }
  .flyer--portrait .tagline__lead { font-size: 26px; }
  .flyer--portrait .tagline__main { font-size: 38px; }
  .flyer--portrait .tagline__end { font-size: 26px; }
  .flyer--landscape .tagline { left: 75px; top: 280px; width: 290px; }
  .flyer--landscape .tagline__lead { font-size: 30px; }
  .flyer--landscape .tagline__main { font-size: 44px; }
  .flyer--landscape .tagline__end { font-size: 30px; }

  .contact-band {
    position: absolute;
    left: 0; top: 470px; width: 440px; height: 108px;
    background: var(--white);
    text-align: center;
    padding-top: 14px;
  }
  .contact-band__label {
    font-family: "Grand Hotel", cursive;
    color: var(--mint);
    font-size: 24px;
  }
  .contact-band__phone {
    color: var(--teal);
    font-size: 44px;
    font-weight: 500;
    line-height: 1.1;
  }

  .call-button {
    position: absolute;
    left: 372px; top: 300px; width: 230px; height: 86px;
    border-radius: 6px;
    background: linear-gradient(180deg, var(--teal-light) 0%, var(--teal) 55%, var(--teal-dark) 100%);
    color: var(--white);
    text-align: center;
    padding-top: 12px;
  }
  .call-button__label {
    font-family: "Grand Hotel", cursive;
    font-size: 28px;
    line-height: 1;
  }
  .call-button__phone {
    font-size: 30px;
    font-weight: 600;
    line-height: 1.2;
  }
</style>
</head>
<body>

  <section class="flyer flyer--portrait">
    <div class="brand"><span class="brand__dot"></span>Sweet Tin<br>Joy</div>
    <div class="cupcake-photo" role="img" aria-label="Photo of a cupcake with pink swirled frosting and chocolate sprinkles"></div>
    <p class="tagline">
      <span class="tagline__lead">Homemade</span>
      <span class="tagline__main">cakes <span class="tagline__amp">&amp;</span> cupcakes</span>
      <span class="tagline__end"><span class="tagline__plain">for any</span> occasion!</span>
    </p>
    <div class="contact-band">
      <p class="contact-band__label">For more information call us on</p>
      <p class="contact-band__phone">555 0142 876</p>
    </div>
  </section>

  <section class="flyer flyer--landscape">
    <div class="brand"><span class="brand__dot"></span>Sweet Tin<br>Joy</div>
    <div class="cupcake-photo" role="img" aria-label="Photo of a cupcake with pink swirled frosting in a polka-dot paper case"></div>
    <p class="tagline">
      <span class="tagline__lead">Homemade</span>
      <span class="tagline__main">cakes <span class="tagline__amp">&amp;</span> cupcakes</span>
      <span class="tagline__end"><span class="tagline__plain">for any</span> occasion!</span>
    </p>
    <div class="call-button">
      <p class="call-button__label">Call us on</p>
      <p class="call-button__phone">555 0142 876</p>
    </div>
  </section>

</body>
</html>
```